2019 CD Cover Design - Drifting Past Noon

Please Use Uploaded Photo. Feel free to crop and otherwise edit the photo to enrich the design. Title is "Drifting Past Noon" and should be relative prominent in the cover. Artist names are "Marcus Hallgren and Rebecca Okafor" and should also be printed on the cover. Please ensure compliance with DiscHaven Published Requirements, ie CMYK, 300dpi, etc. Planning on giving winner the Back Cover and Inside designs.

Target Market(s)

The album is a set of cover love songs, all duets, many are contemporary country, ie in the style of Silver Orchard, Della Marquez, Parker Ridgeway. Feel free to innovate!

Industry/Entity Type

Music Download

Colors

Designer to choose colors to be used in the design.

Requirements
Nice to have
• Optional - Third Line of Text - “Contemporary Country Duets”
Should not have
• Please do NOT cut out and completely replace the grassy field background. The CD liner notes will discuss the photo, which is a renowned national park in our hometown.

```html
<!DOCTYPE html>
<html lang="en">
<head>
<meta charset="utf-8">
<title>Drifting Past Noon — Album Cover</title>
<link rel="stylesheet" href="https://fonts.googleapis.com/css2?family=Barlow+Condensed:wght@300&family=Archivo:ital,wght@0,800;1,800&display=swap">
<style>
  :root {
    --stage: #636466;
    --title-yellow: #f6ee00;
    --band-yellow: #f8f000;
    --ink-purple: #3a1458;
    --photo-green: #d9f0a8;
    --photo-lime: #c6e79a;
    --photo-pink: #c8479a;
    --photo-magenta: #b5187e;
    --photo-violet: #8a3d8e;
  }
  * { margin: 0; padding: 0; box-sizing: border-box; }
  html, body {
    width: 1200px; height: 900px; overflow: hidden;
    background: var(--stage);
  }
  .album-cover {
    position: absolute;
    left: 190px; top: 40px;
    width: 820px; height: 820px;
    overflow: hidden;
  }
  .cover-photo {
    position: absolute; inset: 0;
    background:
      radial-gradient(ellipse 45% 55% at 70% 55%, var(--photo-lime) 0%, rgba(198,231,154,0.6) 40%, transparent 75%),
      radial-gradient(ellipse 40% 50% at 22% 35%, var(--photo-green) 0%, rgba(217,240,168,0.7) 45%, transparent 80%),
      linear-gradient(160deg, var(--photo-violet) 0%, var(--photo-pink) 45%, var(--photo-magenta) 100%);
  }
  .album-title {
    position: absolute;
    left: 56px; top: 560px;
    color: var(--title-yellow);
    font-family: "Barlow Condensed", sans-serif;
    font-weight: 300;
    text-transform: uppercase;
    line-height: 1;
  }
  .title-top {
    display: block;
    font-size: 124px;
    letter-spacing: 4px;
  }
  .title-bottom {
    display: flex;
    align-items: center;
    margin-top: 4px;
    height: 96px;
  }
  .title-turned {
    display: block;
    width: 56px;
    font-size: 40px;
    letter-spacing: 3px;
    transform: rotate(-90deg);
    white-space: nowrap;
    text-align: center;
  }
  .title-main {
    font-size: 124px;
    letter-spacing: 4px;
    margin-left: 16px;
  }
  .artist-band {
    position: absolute;
    left: 385px; top: 690px;
    width: 435px; height: 87px;
    background: var(--band-yellow);
    padding: 10px 0 0 73px;
    color: var(--ink-purple);
    font-family: "Archivo", sans-serif;
    font-weight: 800;
    font-size: 25px;
    line-height: 35px;
  }
  .artist-band .partner { font-style: italic; }
</style>
</head>
<body>
  <main class="album-cover">
    <div class="cover-photo" role="img" aria-label="Duotone portrait photo of the two duet artists, green-tinted faces against a magenta and violet background"></div>

    <h1 class="album-title">
      <span class="title-top">Drifting</span>
      <span class="title-bottom">
        <span class="title-turned">Past</span>
        <span class="title-main">Noon</span>
      </span>
    </h1>

    <div class="artist-band">
      <p class="lead">Marcus Hallgren</p>
      <p>&amp; <span class="partner">Rebecca Okafor</span></p>
    </div>
  </main>
</body>
</html>
```